Professional Sales Business looking for inspirational poster

I need an inspirational poster design for sales professionals, targeted around the phrase "Win Fast, Lose Fast". The style of the poster will be primarily minimalistic and flat with the main focus being on the phrase, however, any graphics or creative font and background styles are encouraged. Color choice is up to you.

Design Specs:
Vector files are best. If creating a vector file isn't possible, 150dpi raster images (at actual size or bigger) are good too. The poster must be in a portrait layout and scalable to the sizes of 18" X 24" and 24" X 36". Please convert all text to outlines.

Please msg me if you have any additional questions.

```html
<!DOCTYPE html>
<html lang="en">
<head>
<meta charset="utf-8">
<title>Win Fast, Lose Fast</title>
<link rel="stylesheet" href="https://fonts.googleapis.com/css2?family=Cinzel:wght@400;500&display=swap">
<style>
  :root {
    --indigo: #3b3a7c;
    --indigo-band: #47478a;
    --side-strip: #4a4a84;
    --side-edge: #3f3f78;
    --ink-white: #ffffff;
  }
  html, body {
    margin: 0;
    padding: 0;
    width: 795px;
    height: 1200px;
    overflow: hidden;
  }
  .poster {
    position: relative;
    width: 795px;
    height: 1200px;
    background: var(--indigo);
    overflow: hidden;
  }
  .side-strip {
    position: absolute;
    left: 0;
    top: 0;
    width: 50px;
    height: 100%;
    background: var(--side-strip);
    border-right: 4px solid var(--side-edge);
  }
  .band {
    position: absolute;
    left: 0;
    width: 100%;
    background: var(--indigo-band);
  }
  .divider {
    position: absolute;
    left: 54px;
    right: 0;
    top: 589px;
    height: 4px;
    background: var(--ink-white);
  }
  .slogan {
    position: absolute;
    left: 151px;
    margin: 0;
    font-family: "Cinzel", "Times New Roman", serif;
    font-weight: 400;
    font-size: 86px;
    line-height: 1;
    color: var(--ink-white);
    letter-spacing: 0;
    white-space: nowrap;
  }
  .slogan--win { top: 458px; }
  .slogan--lose { top: 662px; }
  .thumb {
    position: absolute;
    left: 596px;
    width: 60px;
    height: 115px;
  }
  .thumb--up { top: 416px; }
  .thumb--down { top: 673px; }
  .thumb .hand { fill: var(--ink-white); }
  .thumb .crease { stroke: var(--indigo); stroke-width: 2.5; stroke-linecap: round; fill: none; }
</style>
</head>
<body>
  <main class="poster">
    <div class="band" style="top:120px;height:12px"></div>
    <div class="band" style="top:148px;height:11px"></div>
    <div class="band" style="top:170px;height:11px"></div>
    <div class="band" style="top:199px;height:13px"></div>

    <div class="band" style="top:967px;height:18px"></div>
    <div class="band" style="top:1002px;height:13px"></div>
    <div class="band" style="top:1034px;height:13px"></div>
    <div class="band" style="top:1065px;height:14px"></div>

    <div class="side-strip"></div>

    <h1 class="slogan slogan--win">Win Fast</h1>
    <svg class="thumb thumb--up" viewBox="0 0 60 115" aria-hidden="true">
      <g>
        <rect class="hand" x="0" y="54" width="10" height="60" rx="2"/>
        <path class="hand" d="M14 112 L14 58 Q14 50 20 46 L24 40 L24 8 Q24 0 31 2 Q36 4 36 12 L36 44 L52 44 Q60 44 60 52 Q60 57 56 59 Q60 63 58 68 Q61 73 57 78 Q60 83 57 88 Q59 94 55 98 Q58 106 51 110 L22 114 Q14 114 14 112 Z"/>
        <path class="crease" d="M42 59 L55 59 M42 69 L56 69 M42 79 L56 79 M42 89 L55 89"/>
      </g>
    </svg>

    <div class="divider"></div>

    <h2 class="slogan slogan--lose">Lose Fast</h2>
    <svg class="thumb thumb--down" viewBox="0 0 60 115" aria-hidden="true">
      <g transform="translate(0 115) scale(1 -1)">
        <rect class="hand" x="0" y="54" width="10" height="60" rx="2"/>
        <path class="hand" d="M14 112 L14 58 Q14 50 20 46 L24 40 L24 8 Q24 0 31 2 Q36 4 36 12 L36 44 L52 44 Q60 44 60 52 Q60 57 56 59 Q60 63 58 68 Q61 73 57 78 Q60 83 57 88 Q59 94 55 98 Q58 106 51 110 L22 114 Q14 114 14 112 Z"/>
        <path class="crease" d="M42 59 L55 59 M42 69 L56 69 M42 79 L56 79 M42 89 L55 89"/>
      </g>
    </svg>
  </main>
</body>
</html>
```